Australian residential property business needs a business card design

I need a business card design for my new business 'Meadow Estate Partners'. The business will involve house purchases, land development sites, renovation projects, sub-divisions etc. I will be buying property from motivated vendors and working with property investors. I will deal with a wide range of people working in the residential property market including real estate agents, councils, tradespeople, banks, home owners, etc.

I would like something simple, not flashy, but a little bit unique. The colours should be in line with my logo. The business card needs to be professional. I would like something memorable, but not 'busy' or too bright. Not boring. Modern ok.

Target Market(s)

Home owners looking to sell their property, real estate agents, tradespeople (e.g. plumbers, builders, electricians etc), property investors, local councils, and anyone else involved in the residential property industry

Industry/Entity Type

Business

Contact Information for Business Card

I need to include my business name/logo, my name, my title, a PO Box number/address, a mobile number, and an email address.

Font styles to use
Serif

Requirements
Must have
• My business card details listed above.

```html
<!DOCTYPE html>
<html lang="en">
<head>
<meta charset="utf-8">
<title>Meadow Estate Partners — Business Card</title>
<link href="https://fonts.googleapis.com/css2?family=Ubuntu:wght@400;500;700&display=swap" rel="stylesheet">
<style>
  :root {
    --page-bg: #ecebe8;
    --card-white: #fbfbfa;
    --green-dark: #0f9b4c;
    --green-light: #22b866;
    --accent-orange: #f0a423;
    --rule-red: #e2592d;
    --text-white: #ffffff;
  }
  * { margin: 0; padding: 0; box-sizing: border-box; }
  html, body {
    width: 1200px; height: 1023px; overflow: hidden;
    background: var(--page-bg);
    font-family: "Ubuntu", Arial, sans-serif;
  }
  .stage {
    width: 1200px; height: 1023px;
    display: flex; align-items: center; justify-content: center;
  }
  .business-card {
    position: relative;
    width: 1000px; height: 572px;
    background: var(--card-white);
    box-shadow: 0 10px 30px rgba(0,0,0,0.18);
    overflow: hidden;
  }
  .brand {
    position: absolute; top: 0; left: 0; right: 0; height: 340px;
    display: flex; align-items: center; justify-content: center; gap: 18px;
  }
  .brand-dot {
    width: 34px; height: 34px; border-radius: 50%;
    background: var(--accent-orange);
  }
  .brand-name {
    font-size: 44px; font-weight: 700; letter-spacing: 1px;
    color: var(--accent-orange); text-transform: uppercase;
  }
  .contact-band {
    position: absolute; left: 0; right: 0; bottom: 0; height: 232px;
    background: linear-gradient(100deg, var(--green-dark), var(--green-light));
    border-top: 3px solid var(--rule-red);
  }
  .person {
    position: absolute; left: 70px; bottom: 48px; color: var(--text-white);
  }
  .person-name { font-size: 32px; font-weight: 700; }
  .person-title { font-size: 21px; color: var(--accent-orange); margin-top: 4px; }
  .band-divider {
    position: absolute; left: 520px; top: 40px; bottom: 40px;
    width: 2px; background: var(--accent-orange);
  }
  .contact-list {
    position: absolute; left: 560px; top: 36px;
    list-style: none; color: var(--text-white); font-size: 21px; line-height: 1.55;
  }
  .contact-list li { display: flex; align-items: flex-start; gap: 14px; }
  .contact-list svg { flex: none; margin-top: 6px; }
  .contact-address { padding-left: 34px; }
</style>
</head>
<body>
<main class="stage">
  <article class="business-card">
    <header class="brand">
      <span class="brand-dot"></span>
      <span class="brand-name">Meadow Estate Partners</span>
    </header>
    <section class="contact-band">
      <div class="person">
        <p class="person-name">Danielle Hart</p>
        <p class="person-title">Regional Manager</p>
      </div>
      <div class="band-divider"></div>
      <ul class="contact-list">
        <li>
          <svg width="20" height="20" viewBox="0 0 20 20" aria-hidden="true"><rect x="4" y="1" width="12" height="18" rx="2" fill="none" stroke="#fff" stroke-width="2"/><circle cx="10" cy="15.5" r="1.2" fill="#fff"/></svg>
          <span>0400 555 218</span>
        </li>
        <li>
          <svg width="20" height="20" viewBox="0 0 20 20" aria-hidden="true"><rect x="1" y="4" width="18" height="12" fill="none" stroke="#fff" stroke-width="2"/><path d="M1 4 L10 11 L19 4" fill="none" stroke="#fff" stroke-width="2"/></svg>
          <span>info@meadowestate.com</span>
        </li>
        <li class="contact-address">PO Box 318,</li>
        <li class="contact-address">Orange Grove,</li>
        <li class="contact-address">NSW 2380</li>
      </ul>
    </section>
  </article>
</main>
</body>
</html>
```